Design to promote Vacation Tune Workshop Series for Kids

We are a small local music school in need of a poster design to promote our new Vacation Tune Workshop Series (sort of like a music camp) for the January 2013 Summer Break here in Sydney, Australia.

We generally teach students private instruments (e.g piano, guitar, bass, singing, drums, trumpet and theory) and offer group classes for Glee Club and Group Guitar.

The proposed Vacation Tune Workshop Series goes for 1 week and is 'Jam Packed' with lots of fun musical activities, workshops and musical experiences.

It's called 'Turn The Tunes Loose' and is designed for Kids aged 7 - 12 yrs of age.

We would like an A3 size poster to be designed and an A6 size flyer which compliments the poster. If you're able to also resize the A3 size poster to A4 that'll be great. The successful candidate can do that once the final design is confirmed.

The look and feel should be 'Summer', fun, musical, hip and targeted at young parents aged 28 - 50yrs old. These parents are generally professionals living in a creative area of Sydney.

Text to be included as follows:

'TURN THE TUNES LOOSE'
A Fun Jam Packed Vacation Tune Workshop Series for the Summer Break

Designed for Kids 7 - 12 years old

14 - 18 January, 2013
NEWTOWN

No experience necessary

INSTRUMENTAL DISCOVERY Learn and play a variety of musical instruments
SONG WRITING Write your own songs
BEAT BOXING Learn to beat box and rap
MUSIC GAMES Join in a number of fun musical games and activities
GLEE Do some singing (no problems if you've never tried)
MUSIC TECHNOLOGY Learn about music technology and how to record/produce songs
HAVE FUN!

EARLY BIRD REGISTRATION: $280 per child (when you enrol by 14 December, 2012)

COST: $300 per child
*discounts apply when enrolling 2 or more kids

Goes from Monday - Friday, 9:00am - 3:00pm

ENROL ONLINE NOW
www.brightkeysounds.com.au
Or call 02 7419 2856 / 0438 967 204

For enquiries or more info visit our website or email info@brightkeysounds.com.au

Bright Key Sound School
Unit 4B, 19 Harlow Street, Newtown (enter via Pembrick Ave)

Target Market(s)

Parents of children aged 7 - 12 yrs. They would be around 25 - 50 yrs old

Industry/Entity Type

School

Requirements
Must have
• Must include our company logo - there are two versions which you can pick from to use.

```html
<!DOCTYPE html>
<html lang="en">
<head>
<meta charset="utf-8">
<title>Turn The Tunes Loose – Vacation Tune Workshop Series</title>
<link rel="stylesheet" href="https://fonts.googleapis.com/css2?family=Anton&family=Nunito:wght@400;600;700;800;900&display=swap">
<style>
  :root {
    --orange: #f39325;
    --orange-deep: #ee7d1c;
    --orange-text: #f06c2a;
    --blue: #12a8e4;
    --blue-light: #6fcdf3;
    --yellow: #fff200;
    --white: #ffffff;
    --band: #1ca7df;
  }
  * { margin: 0; padding: 0; box-sizing: border-box; }
  html, body { width: 848px; height: 1200px; overflow: hidden; }
  body { font-family: "Nunito", sans-serif; }

  .poster {
    position: relative;
    width: 848px;
    height: 1200px;
    overflow: hidden;
    background: radial-gradient(circle at 45% 40%, #f8a73a 0%, var(--orange) 55%, var(--orange-deep) 100%);
  }
  .poster > * { z-index: 2; }

  .clef-art {
    position: absolute;
    z-index: 1;
    left: 505px;
    top: 60px;
    width: 325px;
    height: 785px;
    border-radius: 160px 160px 120px 120px;
    background: linear-gradient(160deg, var(--blue-light) 0%, var(--blue) 100%);
  }

  .headline {
    position: absolute;
    left: 44px;
    top: 30px;
    font-family: "Nunito", sans-serif;
    font-weight: 900;
    line-height: 0.92;
    letter-spacing: -3px;
    text-shadow:
      5px 0 0 #fff, -5px 0 0 #fff, 0 5px 0 #fff, 0 -5px 0 #fff,
      4px 4px 0 #fff, -4px 4px 0 #fff, 4px -4px 0 #fff, -4px -4px 0 #fff,
      7px 9px 6px rgba(120, 50, 0, 0.35);
  }
  .headline .line { display: block; font-size: 112px; }
  .headline .line-two { font-size: 100px; }
  .headline .warm { color: var(--orange-text); }
  .headline .cool { color: var(--blue); }

  .tagline {
    position: absolute;
    left: 66px;
    top: 300px;
    transform: rotate(-4deg);
    transform-origin: left top;
    font-weight: 900;
    font-size: 19px;
    line-height: 1.15;
    color: var(--white);
    text-transform: uppercase;
    text-shadow: 1px 2px 2px rgba(120, 50, 0, 0.3);
  }
  .tagline .accent { color: var(--yellow); }

  .details {
    position: absolute;
    left: 50px;
    top: 372px;
    font-weight: 800;
    font-size: 16px;
    color: var(--white);
    text-shadow: 1px 2px 2px rgba(120, 50, 0, 0.3);
  }
  .details .accent { color: var(--yellow); }

  .activities {
    position: absolute;
    left: 48px;
    top: 408px;
    font-family: "Anton", sans-serif;
    text-transform: uppercase;
    line-height: 1;
    text-shadow: 2px 3px 3px rgba(120, 50, 0, 0.3);
  }
  .activities li { list-style: none; display: block; }
  .activities li span { display: inline-block; transform-origin: left center; }
  .activities .hot { color: var(--yellow); }
  .activities .light { color: var(--white); }
  .act-discovery { font-size: 38px; }
  .act-discovery span { transform: scaleX(1.17); }
  .act-song { font-size: 56px; margin-top: 0; }
  .act-song span { transform: scaleX(1.26); }
  .act-beat { font-size: 74px; margin-top: -4px; }
  .act-beat span { transform: scaleX(1.29); }
  .act-games { font-size: 52px; }
  .act-games span { transform: scaleX(1.32); }
  .act-glee { font-size: 124px; line-height: 0.88; margin-top: 4px; }
  .act-glee span { transform: scaleX(1.22); }
  .act-tech { font-size: 44px; }
  .act-tech span { transform: scaleX(1.16); }

  .card {
    position: absolute;
    left: 48px;
    width: 407px;
    background: var(--white);
    border-radius: 8px;
    box-shadow: 2px 3px 6px rgba(120, 50, 0, 0.25);
    text-align: center;
  }
  .enrol-card { top: 798px; height: 183px; padding-top: 14px; }
  .enrol-title { color: var(--orange-text); font-weight: 900; font-size: 22px; }
  .enrol-contact { color: var(--blue); font-weight: 600; font-size: 18px; line-height: 1.25; margin-top: 1px; }
  .price { color: var(--orange-text); font-weight: 900; font-size: 24px; margin-top: 8px; line-height: 1.1; }
  .price-note { color: var(--blue); font-weight: 700; font-size: 13px; }
  .early-bird { color: var(--orange-text); font-weight: 700; font-size: 12px; margin-top: 2px; }

  .brand-card {
    top: 996px;
    height: 101px;
    display: flex;
    align-items: center;
    justify-content: center;
    gap: 18px;
  }
  .brand-name { color: var(--blue); font-weight: 800; font-size: 32px; letter-spacing: -0.5px; }
  .brand-dot { width: 46px; height: 46px; border-radius: 50%; background: var(--orange); }

  .schedule {
    position: absolute;
    left: 480px;
    top: 866px;
    font-weight: 700;
    line-height: 1.3;
  }
  .schedule .label { color: var(--yellow); font-size: 30px; }
  .schedule .time { color: var(--white); font-size: 32px; }

  .venue {
    position: absolute;
    left: 480px;
    top: 1012px;
    font-style: normal;
  }
  .venue-name { color: var(--yellow); font-weight: 700; font-size: 27px; line-height: 1.2; }
  .venue-address { color: var(--white); font-weight: 400; font-size: 17px; line-height: 1.4; }

  .footer-rule {
    position: absolute;
    left: 0; top: 1116px;
    width: 100%; height: 6px;
    background: var(--yellow);
  }
  .footer {
    position: absolute;
    left: 0; top: 1122px;
    width: 100%; height: 78px;
    background: var(--band);
    color: var(--white);
    font-weight: 400;
    font-size: 20.5px;
    display: flex;
    align-items: center;
    justify-content: center;
  }
  .footer .email { color: var(--yellow); margin-left: 6px; }
</style>
</head>
<body>
<main class="poster">
  <div class="clef-art" role="img" aria-label="Large blue treble clef illustration"></div>

  <h1 class="headline">
    <span class="line"><span class="warm">TURN</span> <span class="cool">THE</span></span>
    <span class="line line-two"><span class="cool">TUNES</span> <span class="warm">LOOSE</span></span>
  </h1>

  <p class="tagline">A <span class="accent">fun jam packed</span> vacation tune<br>workshop series for the summer break</p>

  <p class="details">Kids 7 - 12 yrs <span class="accent">·</span> 14 - 18 January, 2013 <span class="accent">·</span> Newtown</p>

  <ul class="activities">
    <li class="act-discovery hot"><span>Instrumental Discovery</span></li>
    <li class="act-song light"><span>Song Writing</span></li>
    <li class="act-beat hot"><span>Beat Boxing</span></li>
    <li class="act-games light"><span>Music Games</span></li>
    <li class="act-glee hot"><span>Glee</span></li>
    <li class="act-tech light"><span>Music Technology</span></li>
  </ul>

  <section class="card enrol-card">
    <p class="enrol-title">ENROL ONLINE NOW!</p>
    <p class="enrol-contact">www.brightkeysounds.com.au<br>Or call 02 7419 2856 / 0438 967 204</p>
    <p class="price">$300 per child</p>
    <p class="price-note">Discounts apply when enrolling 2 or more kids</p>
    <p class="early-bird">Early bird $280 per child when you enrol by 14 December, 2012</p>
  </section>

  <section class="card brand-card">
    <span class="brand-name">brightkeysounds</span>
    <span class="brand-dot"></span>
  </section>

  <div class="schedule">
    <p class="label">Goes from</p>
    <p class="time">Monday - Friday</p>
    <p class="time">9:00am - 3:00pm</p>
  </div>

  <address class="venue">
    <p class="venue-name">Bright Key Sound School</p>
    <p class="venue-address">Unit 4B, 19 Harlow Street, Newtown<br>(Enter via Pembrick Ave)</p>
  </address>

  <div class="footer-rule"></div>
  <footer class="footer">
    For enquiries or more info visit our website or email<span class="email">info@brightkeysounds.com.au</span>
  </footer>
</main>
</body>
</html>
```